Online-Marketing Material für Beraternetzwerk
Zielgruppe
Ich habe ein Beraternetzwerk im deutschen Gesundheitswesen gegründet, gleichzeitig einen gemeinnützigen Verein, habe zwei webseiten www.kv-pflegeberatung-demo.de + www.kv-pflegefreunde-demo.de, Logo, Briefpapier etc. sind vorhanden. Hauptfarbe GmbH RGB 185/87/120 Hex#B95778, Verein RGB 226/125/119 Hex#E27D77. Die Organisationen sind grundsätzlich getrennt, aber es gibt eine Zusammenarbeit und Partner meines Netzwerkes sind auch Fördermitglieder im Verein
Aufgabenstellung
Die beiden Firmenfarben müssen verwendet werden, für die GmbH hauptsächlich die eigene, die 2. Farbe darf mit verwendet werden. Es darf insgesamt feminin wirken, aber nicht verspielt oder gar niedlich. Ich bin Business-Frau;-). Als Schrift habe ich mich auf Avenir next konzentriert, die Agentur hat auch Alternate Gothic auf den Webseiten verwendet. Jetzt benötige ich für eine Veranstaltungsreihe die Ausarbeitung von LinkedIn, Facebook/Insta, Einladung per Brevo und E-Mail Grafiken. Es sind immer Veranstaltungen, zu denen ich einlade und in denen meine Geschäftspartner ihre Expertise gegenüber Kunden darstellen. Die Veranstaltungen sind als Duo zu sehen 1. Präsenz in München, 2. als Online Meeting ein paar Tage später. Die Location wird das Hotel Marwin, direkt am Brunnenhofplatz in München sein. Start der Präsenzveranstaltung 11:00, anschließend Mittagessen. Als Titel für die Veranstaltungen sehe ich 'KlinikForum' vor, es wird jeweils noch ein inhaltliches Thema wie z.B. 'Unternehmenskauf/-verkauf' ergänzt. Erster Termin ist vss. am 15. September 2023. Anbei auch ein paar erste Entwürfe 'meiner' Agentur nebst Feedback von mir. Ich glaube inzwischen nicht, dass hier etwas vernünftiges produziert wird, deshalb mein Versuch auf diesem Weg. Weitere Zusammenarbeit dann herzlich gerne

```html
<!DOCTYPE html>
<html lang="de">
<head>
<meta charset="utf-8">
<title>KlinikForum – Banner</title>
<link rel="stylesheet" href="https://fonts.googleapis.com/css2?family=Montserrat:wght@200;800&family=Nunito+Sans:wght@400;700&display=swap">
<style>
  :root {
    --brand-rose: #C9567F;
    --brand-coral: #D27A82;
    --brand-peach: #DDA186;
    --text-white: #FFFFFF;
    --font-headline: "Montserrat", "Avenir Next", sans-serif;
    --font-body: "Nunito Sans", "Avenir Next", sans-serif;
  }
  html, body {
    margin: 0;
    padding: 0;
    width: 1200px;
    height: 232px;
    overflow: hidden;
    background: #ffffff;
  }
  .banner {
    position: relative;
    width: 1200px;
    height: 232px;
    overflow: hidden;
    background: linear-gradient(90deg, var(--brand-rose) 0%, var(--brand-coral) 50%, var(--brand-peach) 100%);
    color: var(--text-white);
  }
  .banner__headline {
    position: absolute;
    left: 0;
    top: 0;
    width: 1200px;
    height: 190px;
  }
  .headline__text {
    font-family: var(--font-headline);
    font-size: 206px;
    fill: var(--text-white);
  }
  .headline__light { font-weight: 200; }
  .headline__bold { font-weight: 800; }

  .banner__footer {
    position: absolute;
    left: 80px;
    right: 12px;
    bottom: 16px;
    height: 44px;
    display: flex;
    align-items: center;
    gap: 22px;
    font-family: var(--font-body);
  }
  .brand {
    display: flex;
    align-items: center;
    gap: 9px;
  }
  .brand__dot {
    width: 30px;
    height: 30px;
    border-radius: 50%;
    background: var(--text-white);
    flex: none;
  }
  .brand__name {
    font-weight: 700;
    font-size: 14px;
    line-height: 15px;
    letter-spacing: -0.2px;
    color: var(--text-white);
  }
  .contact {
    display: flex;
    align-items: center;
    gap: 12px;
    font-size: 22px;
    font-weight: 400;
    color: var(--text-white);
    white-space: nowrap;
  }
  .contact__sep {
    width: 7px;
    height: 7px;
    border-radius: 50%;
    background: var(--text-white);
  }
</style>
</head>
<body>
  <div class="banner">
    <svg class="banner__headline" viewBox="0 0 1200 190" aria-label="KlinikForum">
      <text class="headline__text" x="12" y="164" textLength="1176" lengthAdjust="spacingAndGlyphs"><tspan class="headline__light">KLINIK</tspan><tspan class="headline__bold" dx="34">FORUM</tspan></text>
    </svg>

    <div class="banner__footer">
      <div class="brand">
        <span class="brand__dot"></span>
        <span class="brand__name">KV Pflegeberatung<br>GmbH</span>
      </div>
      <div class="contact">
        <span class="contact__email">petra.karinwol@kv-pflegeberatung-demo.de</span>
        <span class="contact__sep"></span>
        <span class="contact__web">kv-pflegeberatung-demo.de</span>
      </div>
    </div>
  </div>
</body>
</html>
```